Roll-up display notepad needed for technology-oriented media production company

For a small convention, we need a rollup (85 cm x 200 cm) representing what we offer: media production (video, computer animation, web design, print) for scientifically and technically oriented businesses or organizations. So far, only the logo and a rough idea / layout exist (see attached.,. Png) how to combine bullet points, photographs (see the produced content, see: www.torvapex.com for inspiration with colors, pictures etc .), logo, web adress and so on. This sketch should be taken as a structural guide, it is quite ugly with regards to design, of course. This is where your task begins: Transforming this layout into something fresh. Additionally, we need paper notepads in DIN A7 as a giveway. The attached (only in German, sorry) respectively .ai templates for both the rollup and the notepad should help to deal with the borders / margins necessary for print. So, for additional version of the final vector data should be compatible with AI CS5. If you think you understand the look & amp; feel needed at the interface of science, education & amp; technology on the one hand and marketing on the other hand, we are happy to receive your design suggestions. Do not hesitate to ask questions to clarify the task, if necessary :) Kind regards!

```html
<!DOCTYPE html>
<html lang="de">
<head>
<meta charset="utf-8">
<title>torvapex – Roll-up</title>
<link href="https://fonts.googleapis.com/css2?family=Montserrat:wght@700;800&display=swap" rel="stylesheet">
<style>
  :root {
    --navy: #1f2a3a;
    --slate: #3a4656;
    --steel: #5a6676;
    --paper: #ffffff;
    --film: #2b2b2b;
    --hole: #ffffff;
    --text: #1f2a3a;
  }
  html, body {
    margin: 0;
    padding: 0;
    width: 1200px;
    height: 2821px;
    overflow: hidden;
    background: var(--paper);
  }
  .rollup {
    position: relative;
    width: 1200px;
    height: 2821px;
    overflow: hidden;
    background: var(--paper);
    font-family: "Montserrat", Arial, sans-serif;
  }
  .backdrop {
    position: absolute;
    inset: 0;
    width: 1200px;
    height: 2821px;
  }
  .services {
    position: absolute;
    left: 48px;
    top: 318px;
    margin: 0;
    padding: 0;
    list-style: none;
  }
  .services li {
    position: relative;
    padding-left: 70px;
    height: 118px;
    line-height: 74px;
    font-size: 44px;
    font-weight: 800;
    letter-spacing: 2px;
    color: var(--text);
    text-transform: uppercase;
  }
  .services li::before {
    content: "";
    position: absolute;
    left: 0;
    top: 27px;
    width: 22px;
    height: 22px;
    border-radius: 50%;
    background: var(--text);
  }
  .brand {
    position: absolute;
    left: 780px;
    top: 250px;
    width: 410px;
    text-align: center;
  }
  .brand-circle {
    display: block;
    margin: 0 auto 24px;
    width: 232px;
    height: 232px;
    border: 3px solid var(--navy);
    border-radius: 50%;
    box-sizing: border-box;
  }
  .brand-name {
    font-size: 88px;
    font-weight: 800;
    color: var(--navy);
    line-height: 1;
    letter-spacing: -1px;
  }
</style>
</head>
<body>
<div class="rollup">
  <svg class="backdrop" viewBox="0 0 1200 2821" xmlns="http://www.w3.org/2000/svg">
    <defs>
      <linearGradient id="poly-top" x1="0" y1="0" x2="1" y2="1">
        <stop offset="0" stop-color="#2a3546"/>
        <stop offset="0.5" stop-color="#5a6676"/>
        <stop offset="1" stop-color="#1f2a3a"/>
      </linearGradient>
      <linearGradient id="poly-bottom" x1="0" y1="0" x2="1" y2="1">
        <stop offset="0" stop-color="#4a5666"/>
        <stop offset="0.45" stop-color="#1f2a3a"/>
        <stop offset="0.75" stop-color="#5c6878"/>
        <stop offset="1" stop-color="#27313f"/>
      </linearGradient>
      <radialGradient id="frame-network" cx="0.2" cy="0.5" r="0.9">
        <stop offset="0" stop-color="#d8ecff"/>
        <stop offset="0.3" stop-color="#3f86c9"/>
        <stop offset="1" stop-color="#0c2a52"/>
      </radialGradient>
      <linearGradient id="frame-lab" x1="0" y1="0" x2="1" y2="0">
        <stop offset="0" stop-color="#e6e8ea"/>
        <stop offset="0.5" stop-color="#cfd6d8"/>
        <stop offset="1" stop-color="#2fa08a"/>
      </linearGradient>
      <linearGradient id="frame-title" x1="0" y1="0" x2="0" y2="1">
        <stop offset="0" stop-color="#f2f2f2"/>
        <stop offset="0.3" stop-color="#3a3a3a"/>
        <stop offset="1" stop-color="#2a2a2a"/>
      </linearGradient>
    </defs>

    <polygon class="header-band" role="img" aria-label="Dunkles Polygonmuster als Kopfband"
             points="0,0 1200,0 1200,190 0,38" fill="url(#poly-top)"/>

    <rect class="footer-band" role="img" aria-label="Dunkles Polygonmuster als Hintergrund"
          x="0" y="1900" width="1200" height="921" fill="url(#poly-bottom)"/>

    <g class="film-strip" transform="translate(0,1275) rotate(7.4)">
      <rect x="-120" y="0" width="1460" height="870" fill="var(--film)"/>
      <g class="sprockets" fill="var(--hole)">
        <rect x="-50" y="70" width="56" height="76" rx="8"/>
        <rect x="100" y="70" width="56" height="76" rx="8"/>
        <rect x="250" y="70" width="56" height="76" rx="8"/>
        <rect x="400" y="70" width="56" height="76" rx="8"/>
        <rect x="550" y="70" width="56" height="76" rx="8"/>
        <rect x="700" y="70" width="56" height="76" rx="8"/>
        <rect x="850" y="70" width="56" height="76" rx="8"/>
        <rect x="1000" y="70" width="56" height="76" rx="8"/>
        <rect x="1150" y="70" width="56" height="76" rx="8"/>
        <rect x="-50" y="725" width="56" height="76" rx="8"/>
        <rect x="100" y="725" width="56" height="76" rx="8"/>
        <rect x="250" y="725" width="56" height="76" rx="8"/>
        <rect x="400" y="725" width="56" height="76" rx="8"/>
        <rect x="550" y="725" width="56" height="76" rx="8"/>
        <rect x="700" y="725" width="56" height="76" rx="8"/>
        <rect x="850" y="725" width="56" height="76" rx="8"/>
        <rect x="1000" y="725" width="56" height="76" rx="8"/>
        <rect x="1150" y="725" width="56" height="76" rx="8"/>
      </g>
      <rect class="frame" role="img" aria-label="Blaues Netzwerk aus leuchtenden Knoten"
            x="-120" y="180" width="410" height="510" fill="url(#frame-network)"/>
      <rect class="frame" role="img" aria-label="Laborszene mit Mikroskop und Person im Kittel"
            x="320" y="180" width="720" height="510" fill="url(#frame-lab)"/>
      <rect class="frame" role="img" aria-label="Titelgrafik einer Videoanimation mit Untertitel"
            x="1070" y="180" width="270" height="510" fill="url(#frame-title)"/>
    </g>
  </svg>

  <ul class="services">
    <li>Video</li>
    <li>Computer Animation</li>
    <li>Grafik</li>
    <li>Web &amp; Print</li>
  </ul>

  <div class="brand">
    <span class="brand-circle"></span>
    <div class="brand-name">torvapex</div>
  </div>
</div>
</body>
</html>
```